Pipelining Product Supply Company Needs New Stationery

We need new stationery (letter head, with compliments slips & business card) for our industry leading pipe lining supply company. basically we sell product to other plumbers to carry out pipe relining.

Im looking for something, fresh, professional, sleek and modern at the same time.

Ive attached a copy of the logo and also some guidelines to follow for colours and fonts etc.

Target Market(s)

Plumbers

Industry/Entity Type

Plumbing

Font styles to use
Sans Serif

Requirements
Must have
• The logo, space for ABN, Address, Phone Number, website and email.
Nice to have
• Stand out from the crowd. To look sleep and professional.
Should not have
• Any other colours apart from what is on the guidelines.

```html
<!DOCTYPE html>
<html lang="en">
<head>
<meta charset="utf-8">
<title>Coastal Reline Supplies – Stationery</title>
<link href="https://fonts.googleapis.com/css2?family=Montserrat:wght@400;500;600;700&display=swap" rel="stylesheet">
<style>
  :root{
    --bg:#d0d1d3;
    --green:#8dc63f;
    --green-dark:#5fa52b;
    --ink:#231f20;
    --grey:#7d7e80;
    --grey-light:#a7a9ac;
    --paper:#ffffff;
    --paper-soft:#f3f3f4;
  }
  *{box-sizing:border-box;margin:0;padding:0}
  html,body{width:1200px;height:1200px;overflow:hidden}
  body{background:var(--bg);font-family:"Montserrat",sans-serif;color:var(--ink);position:relative}

  .brand-name{font-family:"Montserrat",sans-serif;font-weight:600;color:var(--green);text-transform:uppercase;white-space:nowrap;letter-spacing:.04em}

  .hero-brand{position:absolute;top:158px;left:0;width:1200px;text-align:center;font-size:30px;line-height:1}

  /* Letterhead */
  .letterhead{position:absolute;left:166px;top:356px;width:476px;height:676px;background:var(--paper);overflow:hidden}
  .letterhead__band{height:7px;background:var(--green)}
  .letterhead__head{position:absolute;top:72px;left:0;width:100%;text-align:center}
  .letterhead__head .brand-name{font-size:12px}
  .letterhead__abn{font-size:8px;color:var(--grey);margin-top:10px;letter-spacing:.03em}
  .letterhead__addr{font-size:5.5px;color:var(--grey);margin-top:6px}
  .letterhead__to{position:absolute;left:72px;top:161px;font-size:7px;font-weight:700}
  .letterhead__date{position:absolute;right:76px;top:161px;font-size:7.5px;color:var(--grey)}
  .letterhead__recipient{position:absolute;left:72px;top:176px}
  .recipient-name{font-size:11px;font-weight:700;letter-spacing:.02em}
  .recipient-role{font-size:7px;color:var(--grey)}
  .letterhead__body{position:absolute;left:72px;top:236px;width:330px;font-size:5.6px;line-height:8.6px;color:#444;text-align:justify}
  .letterhead__body p{margin-bottom:9px}
  .letterhead__body p.lead{font-weight:700;font-size:6.3px;color:var(--ink);letter-spacing:.02em}
  .letterhead__sign{position:absolute;left:72px;top:518px}
  .sign-line{width:74px;height:16px;border-bottom:1px solid var(--ink);margin-bottom:8px}
  .sign-name{font-size:8px;font-weight:700}
  .sign-role{font-size:7px;color:var(--grey)}
  .letterhead__foot{position:absolute;left:0;bottom:0;width:476px;height:100px}
  .letterhead__contacts{position:absolute;left:0;bottom:36px;width:100%;display:flex;justify-content:center;gap:22px;font-size:5.5px;color:var(--paper)}
  .letterhead__contacts span{display:flex;align-items:center;gap:5px}

  /* Business cards */
  .card{position:absolute;width:226px;height:129px;overflow:hidden}
  .card--front{left:619px;top:426px;background:var(--paper-soft);text-align:center}
  .card--front .brand-name{font-size:8.5px;margin-top:54px}
  .card__abn{font-size:4px;color:var(--grey);margin-top:5px}
  .card--back{left:619px;top:598px;background:var(--paper)}
  .card--back svg{position:absolute;left:0;top:0}
  .card__brand{position:absolute;left:8px;top:50px;width:96px;text-align:center}
  .card__brand .brand-name{font-size:7.5px;white-space:normal;line-height:1.25}
  .card__brand .card__abn{font-size:3.5px}
  .card__details{position:absolute;left:120px;top:40px;color:var(--ink)}
  .card__name{font-size:5.5px;font-weight:700}
  .card__role{font-size:4px;color:#3a3a3a;margin-bottom:6px}
  .card__line{display:flex;align-items:center;gap:3px;font-size:3.4px;line-height:7px}
  .dot{width:4px;height:4px;border-radius:50%;background:var(--ink);flex:none}

  /* Compliments slip */
  .slip{position:absolute;left:608px;top:778px;width:472px;height:220px;background:var(--paper);overflow:hidden}
  .slip svg.edge{position:absolute;right:0;top:0}
  .slip__brand{position:absolute;left:42px;top:50px}
  .slip__brand .brand-name{font-size:10px}
  .slip__abn{font-size:7.5px;color:var(--grey);margin-top:14px}
  .slip__contacts{position:absolute;left:42px;top:120px;font-size:7.2px;line-height:11.2px;color:#4a4a4a}
  .slip__ribbon{position:absolute;left:0;top:175px;width:230px;height:29px;background:var(--green);clip-path:polygon(0 0,86% 0,100% 100%,0 100%);color:var(--paper);font-weight:700;font-size:12.5px;letter-spacing:.04em;line-height:29px;padding-left:38px}
</style>
</head>
<body>

<div class="hero-brand brand-name">Coastal Reline Supplies</div>

<section class="letterhead">
  <div class="letterhead__band"></div>
  <header class="letterhead__head">
    <div class="brand-name">Coastal Reline Supplies</div>
    <div class="letterhead__abn">ABN: 12 345 678 901</div>
    <div class="letterhead__addr">14 Harbour Lane Ryde NSW 2112</div>
  </header>
  <div class="letterhead__to">TO:</div>
  <div class="letterhead__date">2.February.2018</div>
  <div class="letterhead__recipient">
    <div class="recipient-name">Your Name</div>
    <div class="recipient-role">Designation</div>
  </div>
  <div class="letterhead__body">
    <p>Lorem Ipsum is simply dummy text of the printing and typesetting industry. Lorem Ipsum has been the industry's standard dummy text ever since the 1500s, when an unknown printer took a galley of type and scrambled it to make a type specimen book. It has survived not only five centuries, but also the leap into electronic typesetting, remaining essentially unchanged. It was popularised in the 1960s with the release of Letraset sheets containing Lorem Ipsum passages, and more recently with desktop publishing software like Aldus PageMaker including versions of Lorem Ipsum.</p>
    <p>Lorem Ipsum is simply dummy text of the printing and typesetting industry. Lorem Ipsum has been the industry's standard dummy text ever since the 1500s, when an unknown printer took a galley of type and scrambled it to make a type specimen book. It has survived not only five centuries, but also the leap into electronic typesetting, remaining essentially unchanged. It was popularised in the 1960s with the release of Letraset sheets containing Lorem Ipsum passages, and more recently with desktop publishing software like Aldus PageMaker including versions of Lorem Ipsum. Lorem Ipsum has been the industry's standard dummy text ever since the 1500s, when an unknown printer took a galley of type and scrambled it to make a type specimen book.</p>
    <p class="lead">Lorem Ipsum is simply dummy text of the printing and typesetting industry. Lorem Ipsum has been the industry's standard dummy text ever since the 1500s, when an unknown printer took a galley of type and scrambled it to make a type specimen book.</p>
    <p>Lorem Ipsum is simply dummy text of the printing and typesetting industry. Lorem Ipsum has been the industry's standard dummy text ever since the 1500s, when an unknown printer took a galley of type and scrambled it to make a type specimen book. It has survived not only five centuries, but also the leap into electronic typesetting, remaining essentially unchanged. It was popularised in the 1960s with the release of Letraset sheets containing Lorem Ipsum passages, and more recently with desktop publishing software like Aldus PageMaker.</p>
  </div>
  <div class="letterhead__sign">
    <div class="sign-line"></div>
    <div class="sign-name">YOUR NAME</div>
    <div class="sign-role">Designation</div>
  </div>
  <svg class="letterhead__foot" viewBox="0 0 476 100" preserveAspectRatio="none">
    <path d="M0 50 Q200 -5 476 18 L476 26 Q220 8 0 56 Z" fill="var(--grey-light)"/>
    <path d="M0 56 Q220 10 476 26 L476 32 Q230 18 0 60 Z" fill="var(--ink)"/>
    <path d="M0 60 Q230 20 476 32 L476 100 L0 100 Z" fill="var(--green)"/>
  </svg>
  <div class="letterhead__contacts">
    <span><svg width="7" height="7" viewBox="0 0 10 10"><path d="M2 1l2 2-1 1.5c.8 1.4 1.6 2.2 3 3L7.5 6l2 2-1.5 1.6C4.5 9.3.7 5.5.4 2.5z" fill="var(--ink)"/></svg>1-300-555-010</span>
    <span><svg width="8" height="6" viewBox="0 0 10 7"><rect x=".5" y=".5" width="9" height="6" fill="none" stroke="var(--ink)"/><path d="M.5.5L5 4 9.5.5" fill="none" stroke="var(--ink)"/></svg>info@coastalreline.com.au</span>
    <span><svg width="7" height="7" viewBox="0 0 10 10"><circle cx="5" cy="5" r="4.4" fill="none" stroke="var(--ink)"/><path d="M.6 5h8.8M5 .6c-2.4 2.6-2.4 6.2 0 8.8M5 .6c2.4 2.6 2.4 6.2 0 8.8" fill="none" stroke="var(--ink)" stroke-width=".7"/></svg>www.coastalreline.com.au</span>
  </div>
</section>

<section class="card card--front">
  <div class="brand-name">Coastal Reline Supplies</div>
  <div class="card__abn">ABN: 12 345 678 901</div>
</section>

<section class="card card--back">
  <svg width="226" height="129" viewBox="0 0 226 129">
    <rect x="0" y="0" width="3" height="129" fill="var(--green)"/>
    <path d="M112 129 Q104 60 116 0 L226 0 L226 129 Z" fill="var(--grey-light)"/>
    <path d="M115 129 Q107 60 119 0 L226 0 L226 129 Z" fill="var(--ink)"/>
    <path d="M119 129 Q110 60 122 0 L226 0 L226 129 Z" fill="var(--green)"/>
  </svg>
  <div class="card__brand">
    <div class="brand-name">Coastal Reline<br>Supplies</div>
    <div class="card__abn">ABN: 12 345 678 901</div>
  </div>
  <div class="card__details">
    <div class="card__name">YOUR NAME</div>
    <div class="card__role">Designation</div>
    <div class="card__line"><span class="dot"></span>1-300-555-010</div>
    <div class="card__line"><span class="dot"></span>info@coastalreline.com.au</div>
    <div class="card__line"><span class="dot"></span>www.coastalreline.com.au</div>
    <div class="card__line"><span class="dot"></span>14 Harbour Lane Ryde NSW 2112</div>
  </div>
</section>

<section class="slip">
  <svg class="edge" width="60" height="220" viewBox="0 0 60 220">
    <path d="M18 220 Q8 80 46 0 L60 0 L60 220 Z" fill="var(--grey-light)"/>
    <path d="M24 220 Q14 80 50 0 L60 0 L60 220 Z" fill="var(--ink)"/>
    <path d="M28 220 Q18 80 53 0 L60 0 L60 220 Z" fill="var(--green)"/>
  </svg>
  <div class="slip__brand">
    <div class="brand-name">Coastal Reline Supplies</div>
    <div class="slip__abn">ABN: 12 345 678 901</div>
  </div>
  <div class="slip__contacts">
    1-300-555-010<br>
    info@coastalreline.com.au<br>
    14 Harbour Lane Ryde NSW 2112<br>
    www.coastalreline.com.au
  </div>
  <div class="slip__ribbon">WITH COMPLIMENTS</div>
</section>

</body>
</html>
```